Red Panda Bamboo Project Postcard Design

My name is Willow Wes.I have been supplying bamboo branches and leaves to a number of zoos including Harrowgate Faunal (Elmcrest Menagerie), Marlow Faunal Society, Quarry Dell Zoo, Fenwick Hill Zoo and ZooKestrel, among others.I also supply bamboo plants to zoos that want to grow bamboo to feed their animals. The bamboo we supply is used predominantly to feed the red pandas.Side note, according to the NFK Ember Fox Lineage Care Plan in section 5, which addresses nutritional requirements, there is a list of bamboo species that are fed to red pandas on page 20. This is a care plan for red pandas which is used by the zoos that belong to the National Faunal Keepers, among others.I have been harvesting and shipping a number of these varieties to many zoos with great results and outstanding feedback, and, since 65%-75% of a red panda’s diet should consist of bamboo, I would like to make your NFK members (and Canadian zoos as well) aware that we strip and ship bamboo branches and leaves within 2 hours of harvest. Typically the bamboo is shipped by SWIFTCART Road and delivered within a few days, depending on distance and urgency. Additionally, we ship or deliver (depending on distance) bamboo plants to zoos that are looking to create a bamboo farm onsite.To give you a little history, I was contacted by Marlow Faunal Society almost a year ago, when they became dissatisfied with the product/services of their previous bamboo supplier. We began supplying MFS, and soon the word spread to other zoos about the quality of the bamboo and the customer service we pride ourselves on, and we received requests to supply them with fresh, high quality bamboo to feed their red pandas and other animals, too. Most of our business in this sector is by word of mouth...We are members of NFK, which is where we want to start with the post card campaign, as well as the Grassland Cane Guild, Federation of Menagerie Gardeners and numerous other organizations.We have a few pictures of red pandas eating the bamboo that I supply, but want to send out a mind blowing postcard to all zoos to promote new business.By the way, my company, Feel the Loam, is the foremost supplier of live bamboo for residential and commercial applications, both indoor and outdoor. We install, remove, maintain bamboo, supply bamboo branches and leaves to zoos for animal feed, and we offer consulting services. Our website, icanecrafter.example, will explain this in more detail.Would like to have pictures of red pandas on the front, or maybe just one incredible one, but we are open to any and all ideas. I have attached a picture that we already have of Pim and Roki with my bamboo, which can be incorporated or not... On the back of the card, I would like to have my logo picture, also attached, to the left of the address section.

Target Market(s)

Zoos: Animal Curators and Caretakers, Nutritionists

Font styles to use
Other font styles liked:
• bamboo letters, is there such a font, or papyrus

Requirements
Must have
• Data from the NFK Ember Fox Lineage Care Plan (Registered document)
Incredible pics of bamboo, red pandas, red pandas eating bamboo, even other animals eating and/or hanging out with bamboo.
Willow Wes's picture on back of card with mailing address below. Logo.
A call to action, ie., call for more information...
Nice to have
• A catchy tag line would be awesome.
Stripped and shipped super-fresh (?)
Maybe, can we superimpose a red panda next to Willow Wes in his picture?
Open to ideas... Maybe 10% off your first order...
Should not have
• Not sure.
You probably know better.

```html
<!DOCTYPE html>
<html lang="en">
<head>
<meta charset="utf-8">
<title>Willow Wes – Postcard</title>
<link rel="stylesheet" href="https://fonts.googleapis.com/css2?family=Oswald:wght@400;600&family=Open+Sans:wght@400;600;700&display=swap">
<style>
  :root{
    --page:#ecebe6;
    --white:#ffffff;
    --green:#7cc242;
    --green-dark:#2f6b2a;
    --green-deep:#1f4d1e;
    --leaf-pale:#eef5e6;
    --ink:#333333;
    --grey:#8a8a8a;
    --line:#b9b9b9;
  }
  *{box-sizing:border-box;margin:0;padding:0}
  html,body{width:900px;height:1200px;overflow:hidden}
  body{background:var(--page);font-family:"Open Sans",Arial,sans-serif;color:var(--ink);position:relative}
  .card{position:absolute;left:40px;width:820px;height:540px;background:var(--white);overflow:hidden;box-shadow:0 2px 10px rgba(0,0,0,.15)}
  .card--front{top:40px;background:linear-gradient(160deg,#ffffff 0%,var(--leaf-pale) 100%)}
  .card--back{top:620px}
  .card svg.shapes{position:absolute;inset:0}
  .brand{position:absolute;display:flex;align-items:center;gap:10px;font-family:"Oswald",Arial,sans-serif;font-weight:600;color:var(--green);text-transform:uppercase;white-space:nowrap}
  .brand__dot{width:22px;height:22px;border-radius:50%;background:var(--green)}
  .card--front .brand{left:40px;top:36px;font-size:34px}
  .tagline{position:absolute;left:40px;top:172px;width:290px;font-family:"Oswald",Arial,sans-serif;text-transform:uppercase;line-height:1;white-space:nowrap}
  .tagline__lead{display:block;font-size:25px;color:var(--green-deep);letter-spacing:.5px}
  .tagline__main{display:block;font-size:50px;color:var(--green);font-weight:600;margin-top:8px;letter-spacing:.5px}
  .website{position:absolute;left:40px;top:300px;font-size:14px;font-weight:700;color:var(--green-deep);letter-spacing:1px}
  .card--back .brand{left:225px;top:120px;font-size:26px}
  .services{position:absolute;left:40px;top:270px;list-style:none;font-size:15px;color:var(--ink);line-height:1.45}
  .services li{position:relative;padding-left:22px}
  .services li::before{content:"";position:absolute;left:0;top:7px;width:10px;height:10px;border-radius:50%;background:var(--green)}
  .contact{position:absolute;left:0;bottom:0;width:410px;height:92px;display:flex;align-items:center;gap:18px;padding:18px 20px 10px 24px;color:var(--white)}
  .contact__call{display:flex;align-items:center;gap:8px}
  .contact__call-text{font-family:"Oswald",Arial,sans-serif;line-height:1.1}
  .contact__call-text b{display:block;font-size:18px;font-weight:600}
  .contact__call-text span{font-size:14px}
  .contact__info{font-size:10px;line-height:1.7}
  .contact__info div{display:flex;align-items:center;gap:5px}
  .message{position:absolute;left:440px;top:70px;width:210px;font-size:12px;line-height:1.5;color:var(--green-dark)}
  .stamp{position:absolute;right:40px;top:38px;width:62px;height:72px;border:2px solid var(--line)}
  .address-lines{position:absolute;left:560px;top:270px;width:220px}
  .address-lines span{display:block;height:38px;border-bottom:2px solid var(--line)}
</style>
</head>
<body>

<section class="card card--front">
  <svg class="shapes" width="820" height="540" viewBox="0 0 820 540">
    <defs>
      <linearGradient id="pandaTone" x1="0" y1="0" x2="1" y2="1">
        <stop offset="0" stop-color="#3d5a2c"/>
        <stop offset=".45" stop-color="#b6532a"/>
        <stop offset="1" stop-color="#5d3b22"/>
      </linearGradient>
      <linearGradient id="caneTone" x1="0" y1="0" x2="1" y2="0">
        <stop offset="0" stop-color="#9bc857"/>
        <stop offset=".5" stop-color="#6fa63a"/>
        <stop offset="1" stop-color="#9cc95a"/>
      </linearGradient>
      <linearGradient id="slothTone" x1="0" y1="0" x2="0" y2="1">
        <stop offset="0" stop-color="#7c6a4c"/><stop offset="1" stop-color="#4a5a34"/>
      </linearGradient>
      <linearGradient id="giantTone" x1="0" y1="0" x2="0" y2="1">
        <stop offset="0" stop-color="#5f7c43"/><stop offset="1" stop-color="#2e3e24"/>
      </linearGradient>
    </defs>
    <rect role="img" aria-label="Stand of green bamboo stalks" x="0" y="360" width="820" height="180" fill="url(#caneTone)"/>
    <path role="img" aria-label="Red panda eating bamboo leaves" d="M380,0 H820 V380 H330 C350,250 345,120 380,0 Z" fill="url(#pandaTone)"/>
    <path d="M380,0 C345,120 350,250 330,380" fill="none" stroke="var(--green)" stroke-width="10"/>
    <circle role="img" aria-label="Sloth among bamboo" cx="440" cy="395" r="58" fill="url(#slothTone)" stroke="#fff" stroke-width="6"/>
    <circle role="img" aria-label="Giant panda eating bamboo" cx="575" cy="415" r="62" fill="url(#giantTone)" stroke="#fff" stroke-width="6"/>
  </svg>
  <div class="brand"><span class="brand__dot"></span>Willow Wes</div>
  <h1 class="tagline">
    <span class="tagline__lead">Stripped and Shipped</span>
    <span class="tagline__main">Super Fresh</span>
  </h1>
  <p class="website">www.icanecrafter.example</p>
</section>

<section class="card card--back">
  <svg class="shapes" width="820" height="540" viewBox="0 0 820 540">
    <defs>
      <linearGradient id="personTone" x1="0" y1="0" x2="0" y2="1">
        <stop offset="0" stop-color="#6f9a45"/><stop offset="1" stop-color="#3f6428"/>
      </linearGradient>
      <linearGradient id="bandTone" x1="0" y1="0" x2="1" y2="0">
        <stop offset="0" stop-color="#1f4d1e"/><stop offset="1" stop-color="#4f9a2e"/>
      </linearGradient>
    </defs>
    <path d="M0,0 H410 C360,60 260,40 190,50 C110,60 40,40 0,70 Z" fill="var(--green)"/>
    <path d="M0,70 C40,40 110,60 190,50 C260,40 360,60 410,0 V12 C360,72 260,56 190,64 C110,72 40,58 0,84 Z" fill="var(--green-dark)"/>
    <rect role="img" aria-label="Willow Wes standing among bamboo plants" x="20" y="60" width="175" height="190" fill="url(#personTone)" stroke="#fff" stroke-width="5"/>
    <path d="M0,470 C120,430 280,455 410,440 V540 H0 Z" fill="url(#bandTone)"/>
  </svg>
  <div class="brand"><span class="brand__dot"></span>Willow Wes</div>
  <ul class="services">
    <li>Bamboo sales</li>
    <li>Bamboo installations</li>
    <li>Bamboo grove management</li>
    <li>Bamboo removal or eradication</li>
    <li>Bamboo control solutions</li>
    <li>Various species and sizes<br>available from 3' to 60'</li>
  </ul>
  <div class="contact">
    <div class="contact__call">
      <svg width="26" height="26" viewBox="0 0 24 24" aria-hidden="true"><path fill="#fff" d="M6.6 10.8a15 15 0 0 0 6.6 6.6l2.2-2.2c.3-.3.7-.4 1-.2 1.1.4 2.3.6 3.6.6.6 0 1 .4 1 1V20c0 .6-.4 1-1 1A17 17 0 0 1 3 4c0-.6.4-1 1-1h3.5c.6 0 1 .4 1 1 0 1.3.2 2.5.6 3.6.1.3 0 .7-.2 1z"/></svg>
      <div class="contact__call-text"><b>CALL NOW</b><span>(555) 010-2218</span></div>
    </div>
    <div class="contact__info">
      <div><svg width="10" height="12" viewBox="0 0 10 14" aria-hidden="true"><path fill="#fff" d="M5 0a5 5 0 0 0-5 5c0 4 5 9 5 9s5-5 5-9a5 5 0 0 0-5-5zm0 7a2 2 0 1 1 0-4 2 2 0 0 1 0 4z"/></svg>Feel the Loam</div>
      <div style="padding-left:15px">12 Reedway Lane, Fernbrook</div>
      <div><svg width="11" height="9" viewBox="0 0 12 9" aria-hidden="true"><path fill="#fff" d="M0 0h12v9H0z M1 1l5 4 5-4" stroke="#3d7a28" stroke-width="1"/></svg>hello@icanecrafter.example</div>
    </div>
  </div>
  <p class="message">Willow Wes will do his best to work within your budget so you can have the fresh, healthy bamboo your animals deserve. Ask about Willow Wes's first order offer.</p>
  <div class="stamp"></div>
  <div class="address-lines"><span></span><span></span><span></span><span></span></div>
</section>

</body>
</html>
```